KVR Biz Cards

We are a property management company that manages luxury level residential estates. As such, we need a business card design that gives a high end feel. The idea at the moment is to list the services offered on the back of the card, and our company information on the front of the card.

Services for the back of the card are as follows:
Professional Property Management service, Home Hosting & Concierge Service, Holliday Home / Income Property Management

```html
<!DOCTYPE html>
<html lang="en">
<head>
<meta charset="utf-8">
<title>KVR Business Card</title>
<link rel="stylesheet" href="https://fonts.googleapis.com/css2?family=Montserrat:wght@400;500;600;700&display=swap">
<style>
  :root {
    --bg: #7f4712;
    --card: #f4f4f4;
    --ink: #111111;
    --brown: #8a5418;
    --brown-faint: #d8cbbb;
  }
  * { margin: 0; padding: 0; box-sizing: border-box; }
  html, body { width: 1200px; height: 1200px; overflow: hidden; }
  body {
    background: var(--bg);
    font-family: "Montserrat", Arial, sans-serif;
    position: relative;
  }
  .card {
    position: absolute;
    left: 180px;
    width: 840px;
    height: 480px;
    background: var(--card);
    border-radius: 56px;
    overflow: hidden;
  }
  .card--front { top: 90px; }
  .card--back { top: 630px; }

  /* Front */
  .brand {
    position: absolute;
    left: 70px;
    top: 150px;
    width: 330px;
  }
  .brand__mark {
    display: flex;
    align-items: center;
    gap: 14px;
    margin-bottom: 18px;
  }
  .brand__square {
    width: 26px; height: 26px;
    background: var(--brown);
  }
  .brand__initials {
    font-size: 52px;
    font-weight: 500;
    color: var(--brown);
    letter-spacing: 2px;
    line-height: 1;
  }
  .brand__name {
    font-size: 25px;
    font-weight: 600;
    color: var(--ink);
    line-height: 1.1;
  }
  .brand__tagline {
    font-size: 16px;
    font-weight: 400;
    color: var(--brown);
    margin-top: 4px;
  }
  .divider {
    position: absolute;
    left: 430px;
    top: 95px;
    width: 3px;
    height: 290px;
    background: var(--brown);
  }
  .person {
    position: absolute;
    right: 60px;
    top: 110px;
    text-align: right;
  }
  .person__name {
    font-size: 40px;
    font-weight: 600;
    color: var(--ink);
    letter-spacing: 1px;
  }
  .person__role {
    font-size: 24px;
    font-weight: 600;
    color: var(--brown);
  }
  .contact {
    position: absolute;
    left: 475px;
    top: 240px;
    list-style: none;
  }
  .contact__item {
    display: flex;
    align-items: center;
    gap: 12px;
    font-size: 15px;
    font-weight: 500;
    color: var(--ink);
    margin-bottom: 14px;
  }
  .contact__icon { width: 20px; height: 20px; flex: none; }

  /* Back */
  .back-brand {
    position: absolute;
    left: 0; right: 0;
    top: 110px;
    text-align: center;
  }
  .back-brand__name {
    font-size: 44px;
    font-weight: 600;
    color: var(--ink);
    letter-spacing: 1px;
    line-height: 1.2;
  }
  .back-brand__tagline {
    font-size: 27px;
    font-weight: 400;
    color: var(--brown);
    line-height: 1.3;
  }
  .back-initials {
    position: absolute;
    left: 0; right: 0;
    top: 232px;
    text-align: center;
    font-size: 110px;
    font-weight: 500;
    color: var(--brown-faint);
    letter-spacing: 8px;
    line-height: 1;
  }
  .services {
    position: absolute;
    left: 0; right: 0;
    bottom: 52px;
    text-align: center;
    font-size: 16px;
    font-weight: 600;
    color: var(--brown);
    line-height: 1.5;
  }
</style>
</head>
<body>

<section class="card card--front">
  <div class="brand">
    <div class="brand__mark">
      <span class="brand__square"></span>
      <span class="brand__initials">KVR</span>
    </div>
    <p class="brand__name">KOVARI MANAGEMENT</p>
    <p class="brand__tagline">Crafted Care for Every Residence</p>
  </div>

  <div class="divider"></div>

  <div class="person">
    <p class="person__name">DANIEL REYES</p>
    <p class="person__role">Manager</p>
  </div>

  <ul class="contact">
    <li class="contact__item">
      <svg class="contact__icon" viewBox="0 0 20 20"><circle cx="10" cy="10" r="10" fill="#8a5418"/><circle cx="10" cy="10" r="5.5" fill="none" stroke="#fff" stroke-width="1.3"/><path d="M4.5 10h11M10 4.5c-2.5 3-2.5 8 0 11M10 4.5c2.5 3 2.5 8 0 11" fill="none" stroke="#fff" stroke-width="1.1"/></svg>
      www.kovarihome.com
    </li>
    <li class="contact__item">
      <svg class="contact__icon" viewBox="0 0 20 20"><circle cx="10" cy="10" r="10" fill="#8a5418"/><rect x="7" y="4.5" width="6" height="11" rx="1.2" fill="#fff"/><rect x="8" y="6" width="4" height="7" fill="#8a5418"/></svg>
      +000 000 000
    </li>
    <li class="contact__item">
      <svg class="contact__icon" viewBox="0 0 20 20"><circle cx="10" cy="10" r="10" fill="#8a5418"/><rect x="5" y="6.5" width="10" height="7" rx="1" fill="#fff"/><path d="M5.5 7l4.5 3.5L14.5 7" fill="none" stroke="#8a5418" stroke-width="1.2"/></svg>
      hello@kovarihome.com
    </li>
    <li class="contact__item">
      <svg class="contact__icon" viewBox="0 0 20 20"><circle cx="10" cy="10" r="10" fill="#8a5418"/><path d="M10 15.5s-4-4-4-7a4 4 0 0 1 8 0c0 3-4 7-4 7z" fill="#fff"/><circle cx="10" cy="8.5" r="1.5" fill="#8a5418"/></svg>
      Lorem ipsum dolor , consectetuer
    </li>
  </ul>
</section>

<section class="card card--back">
  <div class="back-brand">
    <p class="back-brand__name">KOVARI MANAGEMENT</p>
    <p class="back-brand__tagline">Crafted Care for Every Residence</p>
  </div>
  <p class="back-initials" aria-hidden="true">KVR</p>
  <p class="services">
    • Full-Service Estate Management • Guest Hosting &amp; Concierge Care<br>
    • Vacation Home • Rental Property Oversight
  </p>
</section>

</body>
</html>
```